Business Card Design Project

New business card design front and back for IT company that does network support and web design.
Calloway IT
Doug Calloway
Managing Director
PO Box 918 Brinsley VIC 3421
doug@callowayit.example
www.callowayit.example

Industry/Entity Type

Business

```html
<!DOCTYPE html>
<html lang="en">
<head>
<meta charset="utf-8">
<title>Calloway IT – Business Cards</title>
<link rel="stylesheet" href="https://fonts.googleapis.com/css2?family=Mulish:wght@400;500;800&display=swap">
<style>
  :root {
    --backdrop: #4a4746;
    --brand-blue: #00a6d3;
    --brand-blue-deep: #0090bb;
    --brand-blue-light: #22b8e0;
    --band-black: #19191b;
    --card-charcoal: #333335;
    --card-charcoal-dark: #232325;
    --text-dark: #1b1b1d;
    --text-light: #ffffff;
    --text-muted: #e4e4e4;
  }
  * { box-sizing: border-box; margin: 0; padding: 0; }
  html, body {
    width: 1200px; height: 848px; overflow: hidden;
    background: var(--backdrop);
    font-family: "Mulish", "Helvetica Neue", Arial, sans-serif;
  }
  .canvas { position: relative; width: 1200px; height: 848px; }

  .card {
    position: absolute; width: 536px; height: 297px; overflow: hidden;
    box-shadow: 0 2px 6px rgba(0,0,0,0.35);
  }

  /* Contact side */
  .card--contact { left: 238px; top: 117px; background: linear-gradient(180deg, var(--card-charcoal) 0%, var(--card-charcoal-dark) 100%); }
  .contact__header {
    position: absolute; left: 0; top: 0; width: 100%; height: 99px;
    background: radial-gradient(ellipse at 85% 0%, var(--brand-blue-deep) 0%, var(--brand-blue) 45%, var(--brand-blue-light) 100%);
  }
  .contact__brand {
    position: absolute; left: 34px; top: 38px;
    color: var(--text-light); font-weight: 800; font-size: 20px; letter-spacing: 0.5px;
  }
  .contact__name {
    position: absolute; left: 218px; top: 71px;
    color: var(--text-dark); font-size: 22px; font-weight: 500; letter-spacing: 0.6px;
  }
  .contact__title-band {
    position: absolute; left: 0; top: 99px; width: 100%; height: 34px;
    background: var(--band-black);
  }
  .contact__title {
    position: absolute; left: 218px; top: 6px;
    color: var(--text-light); font-size: 15px; letter-spacing: 0.4px;
  }
  .contact__list { position: absolute; left: 185px; top: 151px; list-style: none; }
  .contact__item {
    display: flex; align-items: center; height: 23px;
    color: var(--text-muted); font-size: 15.5px; letter-spacing: 0.5px;
  }
  .contact__icon { width: 20px; height: 14px; margin-right: 13px; flex: none; }
  .contact__icon-text { width: 20px; margin-right: 13px; color: var(--brand-blue); font-weight: 800; font-size: 15px; text-align: center; }

  /* Brand side */
  .card--brand {
    left: 431px; top: 453px;
    background: radial-gradient(ellipse at 90% 5%, var(--brand-blue-deep) 0%, var(--brand-blue) 40%, var(--brand-blue-light) 100%);
  }
  .brand__name {
    position: absolute; left: 0; top: 142px; width: 100%; text-align: center;
    color: var(--text-light); font-weight: 800; font-size: 29px; letter-spacing: 0.3px;
  }
  .brand__tagline {
    position: absolute; left: 0; top: 188px; width: 100%; text-align: center;
    color: var(--text-dark); font-size: 15px; letter-spacing: 0.6px;
  }
</style>
</head>
<body>
<main class="canvas">

  <section class="card card--contact" aria-label="Business card, contact side">
    <div class="contact__header">
      <span class="contact__brand">Calloway IT</span>
      <span class="contact__name">Doug Calloway</span>
    </div>
    <div class="contact__title-band">
      <span class="contact__title">Managing Director</span>
    </div>
    <ul class="contact__list">
      <li class="contact__item">
        <svg class="contact__icon" viewBox="0 0 20 14" aria-hidden="true">
          <rect x="1.5" y="1.5" width="17" height="11" fill="none" stroke="#00a6d3" stroke-width="1.6"/>
          <polyline points="1.5,1.5 10,8 18.5,1.5" fill="none" stroke="#00a6d3" stroke-width="1.6"/>
        </svg>
        PO Box 918 Brinsley VIC 3421
      </li>
      <li class="contact__item">
        <svg class="contact__icon" viewBox="0 0 20 14" aria-hidden="true">
          <path d="M3 11 C1 8 3 4 7 3 L14 2 C17 2 19 4 18 6 L15 7 L14 5 L8 6 C6 7 6 9 7 10 L5 12 Z" fill="none" stroke="#00a6d3" stroke-width="1.5" stroke-linejoin="round"/>
        </svg>
        0400 555 182
      </li>
      <li class="contact__item"><span class="contact__icon-text">@</span>doug@callowayit.example</li>
      <li class="contact__item"><span class="contact__icon-text">w</span>www.callowayit.example</li>
    </ul>
  </section>

  <section class="card card--brand" aria-label="Business card, brand side">
    <h1 class="brand__name">CALLOWAY IT</h1>
    <p class="brand__tagline">IT SOLUTIONS FOR YOUR BUSINESS</p>
  </section>

</main>
</body>
</html>
```